We are looking to design a black on white bourbon label for a new brand
in att we have added
1. the bottle we need to use (wine bottle in black)
2. some industry examples (Look at horse rider label good example of where we need to go)
3. horses and cowboys illistrations

The brand will be Called OLD BRASS LANTERN. we want an old school feeling label prohibition style.

What we need on the label is
1. visual = Bucking Horse + rider cowboy + lasso forming a circle
2. Name = Old Brass Lantern Bourbon Straight Aged Whiskey
3. Product info = 70 CL 40 ABV
4. Distilled in the Wild Wild West WWW.OLDBRASSLANTERNSPIRITS.COM

```html
<!DOCTYPE html>
<html lang="en">
<head>
<meta charset="utf-8">
<title>Old Brass Lantern – Bourbon Label</title>
<link rel="stylesheet" href="https://fonts.googleapis.com/css2?family=Cormorant+SC:wght@500;600&display=swap">
<style>
  :root {
    --backdrop: #3a3a3a;
    --label-black: #1d1d1d;
    --ink-white: #f2f2f0;
    --ink-soft: #bdbdbb;
    --rule: #8a8a88;
    --art-light: #7a7a78;
    --art-dark: #262626;
  }
  * { margin: 0; padding: 0; box-sizing: border-box; }
  html, body {
    width: 1200px;
    height: 815px;
    overflow: hidden;
    background: var(--backdrop);
  }
  .canvas {
    width: 1200px;
    height: 815px;
    display: flex;
    align-items: center;
    justify-content: center;
  }
  .label {
    width: 440px;
    height: 760px;
    background: var(--label-black);
    border-radius: 6px;
    display: flex;
    flex-direction: column;
    align-items: center;
    padding-top: 56px;
    color: var(--ink-white);
    font-family: "Cormorant SC", "Times New Roman", serif;
  }
  .brand-name {
    font-size: 38px;
    font-weight: 600;
    letter-spacing: 4px;
    line-height: 1;
    text-align: center;
    white-space: nowrap;
  }
  .artwork {
    width: 300px;
    height: 300px;
    margin-top: 40px;
    border-radius: 50%;
    background: radial-gradient(circle at 50% 45%, var(--art-light) 0%, var(--art-dark) 100%);
  }
  .product-info {
    width: 300px;
    display: flex;
    justify-content: space-between;
    font-size: 14px;
    font-weight: 600;
    letter-spacing: 1px;
    margin-top: 44px;
  }
  .rule {
    width: 320px;
    height: 1px;
    background: var(--rule);
  }
  .rule.top { margin-top: 14px; }
  .product-name {
    font-size: 27px;
    font-weight: 600;
    letter-spacing: 3px;
    line-height: 1.35;
    text-align: center;
    margin: 18px 0 20px;
  }
  .rule.double {
    height: 4px;
    background: none;
    border-top: 1px solid var(--rule);
    border-bottom: 1px solid var(--rule);
  }
  .origin {
    font-size: 15px;
    font-weight: 500;
    letter-spacing: 5px;
    margin-top: 14px;
    color: var(--ink-soft);
  }
  .website {
    font-size: 10px;
    letter-spacing: 2px;
    margin-top: 6px;
    margin-bottom: 10px;
    color: var(--ink-soft);
  }
</style>
</head>
<body>
<main class="canvas">
  <section class="label">
    <h2 class="brand-name">Old Brass Lantern</h2>
    <div class="artwork" role="img"
         aria-label="Illustration of a cowboy riding a bucking horse, framed by a coiled lasso forming a circle"></div>

    <div class="product-info">
      <span class="volume">70 CL</span>
      <span class="strength">40% ABV</span>
    </div>
    <div class="rule top"></div>
    <h1 class="product-name">Bourbon Straight<br>Aged Whiskey</h1>
    <div class="rule double"></div>
    <p class="origin">Distilled In The Wild West</p>
    <p class="website">WWW.OLDBRASSLANTERNSPIRITS.COM</p>
    <div class="rule"></div>
  </section>
</main>
</body>
</html>
```